Makeup artist looking for business card design

- Business card to be memorable and recognisable

- I've attached photos of my logo (File 4), photos that I want to incorporate into the design (File 5,6 & 7) and an example of the design I like "Mirela Stott" (File 1)

- I've attached 3 photos of the designs I want to use, please use one of your choice

- Next to Instagram (File 2) and Facebook (File 3), please use their logo.

- No coloured background, either use the original background (grey) old white.

- Please include the following on the business card:
- Business name: LK Makeup Artistry
- My name: Rosalind Kerr
- Occupation: Makeup Artist
- Contact number: 0437 295 148
- Email: roskerr_makeup@mailvento.com
- Instagram (please use image): @lkmakeupartistry
- Facebook (please use image): www.facebook.com/LKMakeUpArtistry

Target Market(s)

Target woman for bridal makeup, occasion, fashion makeup and print.

Industry/Entity Type

Business

Requirements
Must have
• Logo provided and photo provided
Should not have
• Colourful background
Too cluttered
Shouldn't use old style font

```html
<!DOCTYPE html>
<html lang="en">
<head>
<meta charset="utf-8">
<title>LK Makeup Artistry – Business Card</title>
<link rel="stylesheet" href="https://fonts.googleapis.com/css2?family=Questrial&display=swap">
<style>
  :root {
    --page-bg: #e9e7e6;
    --card-white: #ffffff;
    --band-black: #050505;
    --rose: #d4a3c4;
    --rose-line: #d7a7c7;
    --ink-grey: #5e5a5d;
    --lavender: #b79bc8;
    --lavender-deep: #8d6aa8;
    --petal-white: #f3eef5;
    --skin: #e2c0ae;
    --hair: #3a2a22;
    --icon-fill: #d9aecb;
  }
  * { margin: 0; padding: 0; box-sizing: border-box; }
  html, body {
    width: 1200px;
    height: 1000px;
    overflow: hidden;
    background: var(--page-bg);
    font-family: "Questrial", "Century Gothic", sans-serif;
  }
  .canvas {
    position: relative;
    width: 1200px;
    height: 1000px;
  }
  .card {
    position: absolute;
    top: 154px;
    width: 435px;
    height: 726px;
    border-radius: 28px;
    overflow: hidden;
  }
  .card--front {
    left: 146px;
    background: var(--band-black);
  }
  .card--back {
    left: 581px;
    background: var(--card-white);
    text-align: center;
  }
  .front__photo {
    position: absolute;
    left: 0; top: 0;
    width: 435px;
    height: 658px;
    background:
      radial-gradient(ellipse 150px 200px at 170px 300px, var(--skin) 0%, rgba(226,192,174,0.6) 55%, rgba(226,192,174,0) 100%),
      radial-gradient(ellipse 220px 140px at 140px 60px, var(--hair) 0%, rgba(58,42,34,0) 100%),
      radial-gradient(ellipse 220px 300px at 380px 500px, var(--lavender-deep) 0%, rgba(141,106,168,0) 100%),
      linear-gradient(160deg, #d9cfdc 0%, var(--petal-white) 45%, var(--lavender) 100%);
  }
  .front__rule {
    position: absolute;
    left: 0; top: 658px;
    width: 435px;
    height: 6px;
    background: var(--rose-line);
  }
  .front__band {
    position: absolute;
    left: 0; top: 664px;
    width: 435px;
    height: 62px;
    display: flex;
    align-items: center;
    justify-content: center;
  }
  .front__business-name {
    color: var(--rose);
    font-size: 33px;
    letter-spacing: 1px;
    word-spacing: 6px;
    text-transform: uppercase;
  }
  .back__wordmark {
    position: absolute;
    left: 0; right: 0;
    top: 190px;
    display: flex;
    align-items: center;
    justify-content: center;
    gap: 12px;
  }
  .back__wordmark-dot {
    width: 14px;
    height: 14px;
    border-radius: 50%;
    background: var(--ink-grey);
  }
  .back__wordmark-text {
    color: var(--ink-grey);
    font-size: 26px;
    letter-spacing: 2px;
    text-transform: uppercase;
  }
  .back__name {
    position: absolute;
    left: 0; right: 0;
    top: 310px;
    color: var(--rose);
    font-size: 32px;
    letter-spacing: 1px;
    text-transform: uppercase;
  }
  .back__role {
    position: absolute;
    left: 0; right: 0;
    top: 350px;
    color: var(--ink-grey);
    font-size: 29px;
    word-spacing: 4px;
  }
  .back__contact {
    position: absolute;
    left: 0; right: 0;
    top: 500px;
    color: var(--ink-grey);
    font-size: 22px;
    line-height: 26px;
  }
  .contact-line {
    display: flex;
    align-items: center;
    justify-content: center;
    gap: 6px;
  }
  .contact-line svg { width: 15px; height: 15px; }
  .back__social {
    position: absolute;
    left: 0; right: 0;
    top: 640px;
    display: flex;
    justify-content: center;
    align-items: flex-end;
    color: var(--ink-grey);
    font-size: 20px;
  }
  .social-item {
    display: flex;
    flex-direction: column;
    align-items: center;
    gap: 8px;
  }
  .social-item__badge {
    width: 32px;
    height: 32px;
    border-radius: 5px;
    background: var(--ink-grey);
  }
  .social-divider {
    margin: 0 7px 2px;
    width: 2px;
    height: 24px;
    background: var(--ink-grey);
  }
</style>
</head>
<body>
<main class="canvas">
  <section class="card card--front">
    <div class="front__photo" role="img" aria-label="Portrait of a model wearing lavender eye makeup and lilac lipstick, framed by purple and white flower petals"></div>
    <div class="front__rule"></div>
    <div class="front__band">
      <span class="front__business-name">LK Makeup Artistry</span>
    </div>
  </section>

  <section class="card card--back">
    <div class="back__wordmark">
      <span class="back__wordmark-dot"></span>
      <span class="back__wordmark-text">LK Makeup Artistry</span>
    </div>

    <h1 class="back__name" style="font-weight:400">Rosalind Kerr</h1>
    <p class="back__role">Makeup Artist</p>

    <div class="back__contact">
      <p class="contact-line">
        <svg viewBox="0 0 16 16" aria-hidden="true">
          <circle cx="8" cy="8" r="8" fill="var(--icon-fill)"/>
          <rect x="5.5" y="3.5" width="5" height="9" rx="1" fill="none" stroke="#fff" stroke-width="1.2"/>
        </svg>
        <span>0437 295 148</span>
      </p>
      <p class="contact-line">
        <svg viewBox="0 0 16 16" aria-hidden="true">
          <circle cx="8" cy="8" r="8" fill="var(--icon-fill)"/>
          <rect x="4" y="5" width="8" height="6" fill="none" stroke="#fff" stroke-width="1.1"/>
          <path d="M4 5 L8 8.5 L12 5" fill="none" stroke="#fff" stroke-width="1.1"/>
        </svg>
        <span>roskerr_makeup@mailvento.com</span>
      </p>
    </div>

    <div class="back__social">
      <div class="social-item">
        <span class="social-item__badge"></span>
        <span>@lkmakeupartistry</span>
      </div>
      <span class="social-divider"></span>
      <div class="social-item">
        <span class="social-item__badge"></span>
        <span>LKMakeUpArtistry</span>
      </div>
    </div>
  </section>
</main>
</body>
</html>
```